Postcard Flyer For Plumbing Company

We are a p[professional plumbing company in NSW that carry out plumbing, electrical and hot water system work.
i want to send a postcard size flyer 105mm x 148mm to our clients to offer $xx off their next job they book with us.
The front of the flyer needs to say.... Feel The Love WIth $35 Off your Next Job. It needs to include a section where their name and postal address can go (74mm W x 24mm H) on the left hand side of the bottom of the flyer - refer attached example.
The other side of the flyer needs to have a section for text, the offer ($35 or $xx what they get off their next job) and also can use the tag line... Call 1 Number for The Best In 3 Trades - Plumbing, Hot Water & Electrical.
Plumbing, hot water and electrical pictures/icons can be used.
I want the flyer to stand out, use the corporate colours and be modern whilst letting them know that they can use this voucher on their next job.
Refer attachments.

Target Market(s)

Homeowners and our existing clients

Industry/Entity Type

Plumbing

Font styles to use
Serif

Colors
0255a3
ec1f27
ffffff
d3d3d3

Requirements
Must have
• Corporate colours and logos
• Red Colour:
• C=0
• M=100
• Y=100
• K=0
• Blue Colour
• C= 100
• M=66
• Y=0
• K=2
• Grey Colour
• C= 26
• M=21
• Y=19
• K=0
Nice to have
• predominately white background
Should not have
• Black background and lots of black.

```html
<!DOCTYPE html>
<html lang="en">
<head>
<meta charset="utf-8">
<title>Harbour Trades – $35 Off Postcard</title>
<link rel="stylesheet" href="https://fonts.googleapis.com/css2?family=Yellowtail&family=Montserrat:wght@400;500;700&family=Roboto:wght@400;700;900&display=swap">
<style>
:root{
  --orange:#e5692f;
  --sky:#a9d5e2;
  --sky-line:#7fbccd;
  --blue:#0d3f94;
  --blue-dark:#082c6e;
  --red:#c8282a;
  --yellow:#f6c21a;
  --white:#ffffff;
  --ink:#2b2b2b;
  --grey:#d3d3d3;
}
*{margin:0;padding:0;box-sizing:border-box}
html,body{width:774px;height:1200px;overflow:hidden;background:var(--white)}
body{position:relative;font-family:"Roboto",Arial,sans-serif;color:var(--ink)}
.abs{position:absolute}
.panel{position:absolute;left:0;width:774px;overflow:hidden}
.front{top:0;height:600px}
.back{top:600px;height:600px}
.photo{position:absolute}
.script{font-family:"Yellowtail",cursive;color:var(--white);position:absolute;line-height:1;white-space:nowrap}
.headline-amount{position:absolute;font-family:"Montserrat",Arial,sans-serif;font-weight:500;color:var(--white);line-height:1}
.services-lead{position:absolute;left:32px;top:340px;font-family:"Montserrat",sans-serif;font-size:15px;color:var(--white)}
.services-row{position:absolute;left:32px;top:362px;font-family:"Roboto",sans-serif;font-weight:700;font-size:17px;color:var(--white);letter-spacing:.2px;word-spacing:2px;white-space:nowrap}
.services-row span{margin:0 16px}
.brand{position:absolute;left:536px;width:216px;text-align:center}
.brand-name{font-family:"Roboto",sans-serif;font-weight:900;font-size:30px;color:var(--blue);line-height:1.1;letter-spacing:.5px}
.brand-tag{font-family:"Roboto",sans-serif;font-weight:700;font-size:13px;color:var(--ink);margin-top:10px;white-space:nowrap}
.call-word{left:96px;top:40px;font-size:54px}
.one-number{left:30px;top:84px;font-size:60px;width:300px;overflow:visible}
.tagline-sub{position:absolute;left:86px;top:136px;font-family:"Montserrat",sans-serif;font-size:20px;color:var(--white);white-space:nowrap}
.brief-title{position:absolute;left:32px;top:172px;font-family:"Montserrat",sans-serif;font-size:15px;color:var(--white)}
.brief-list{position:absolute;left:32px;top:202px;list-style:none;width:310px}
.brief-list li{position:relative;padding-left:22px;font-family:"Montserrat",sans-serif;font-size:13px;line-height:15.5px;color:var(--white);margin-bottom:6px;white-space:nowrap}
.brief-list li svg{position:absolute;left:0;top:3px}
.trade-label{position:absolute;font-family:"Roboto",sans-serif;font-weight:900;font-size:20px;text-align:center;line-height:34px;box-shadow:2px 3px 4px rgba(0,0,0,.25);white-space:nowrap}
.label-plumbing{background:var(--blue);color:var(--white);transform:rotate(-3deg)}
.label-hotwater{background:var(--yellow);color:var(--red)}
.label-electrical{background:var(--red);color:var(--white);transform:rotate(2deg)}
.voucher-note{position:absolute;left:620px;top:380px;font-size:12px;color:var(--white);line-height:14px;white-space:nowrap}
.contact{position:absolute;left:38px;list-style:none}
.contact li{position:absolute;left:0;white-space:nowrap;font-family:"Roboto",sans-serif;color:#444}
.contact li svg{position:absolute;left:0}
.contact li span{position:absolute;left:21px}
</style>
</head>
<body>

<section class="panel front">
  <div class="abs" style="left:0;top:0;width:430px;height:600px;background:var(--orange)"></div>
  <div class="abs" style="left:470px;top:0;width:304px;height:600px;background:var(--sky)"></div>
  <svg class="abs" style="left:470px;top:0" width="304" height="440" aria-hidden="true">
    <g fill="none" stroke="var(--sky-line)" stroke-width="3" opacity=".8">
      <rect x="20" y="24" width="82" height="90"/><rect x="120" y="24" width="82" height="90"/>
      <rect x="20" y="132" width="82" height="90"/><rect x="120" y="240" width="82" height="90"/>
      <rect x="20" y="240" width="82" height="90"/><rect x="220" y="300" width="82" height="90"/>
    </g>
  </svg>
  <svg class="abs" style="left:418px;top:0" width="66" height="420" aria-hidden="true">
    <rect x="6" y="0" width="54" height="420" fill="var(--blue)"/>
    <rect x="6" y="0" width="10" height="420" fill="var(--blue-dark)"/>
    <rect x="0" y="92" width="66" height="62" rx="4" fill="var(--blue)"/>
    <rect x="0" y="92" width="66" height="8" rx="3" fill="var(--blue-dark)"/>
    <rect x="0" y="146" width="66" height="8" rx="3" fill="var(--blue-dark)"/>
  </svg>

  <div class="photo" role="img" aria-label="Technician servicing an outdoor air-conditioning unit" style="left:23px;top:236px;width:90px;height:96px;background:linear-gradient(135deg,#5a6470,#2f3640);border:4px solid #f08a52"></div>
  <div class="photo" role="img" aria-label="Smiling tradesman in hard hat and navy work shirt holding an orange cable coil" style="left:276px;top:72px;width:200px;height:320px;background:linear-gradient(180deg,#e97b3e 0%,#1f2a44 35%,#1a2238 100%);border-radius:90px 90px 0 0"></div>
  <div class="photo" role="img" aria-label="Plumber in blue fixing pipes under a sink with a wrench" style="left:588px;top:28px;width:164px;height:184px;background:linear-gradient(135deg,#3f6fb5,#cfd6dc 60%,#8a8f94)"></div>
  <div class="photo" role="img" aria-label="Illustrated hand holding an adjustable wrench" style="left:564px;top:156px;width:210px;height:172px;background:linear-gradient(150deg,#2a2a2a 0%,#2a2a2a 30%,#f0b07a 55%,#1f4fa0 100%);opacity:.9;border-radius:40px 0 0 60px"></div>
  <div class="photo" role="img" aria-label="Close-up of a chrome tap" style="left:496px;top:328px;width:74px;height:82px;background:linear-gradient(135deg,#dfe3e6,#6c747b)"></div>

  <div class="script" style="left:28px;top:62px;font-size:42px;transform:rotate(-14deg);transform-origin:left bottom">Feel the love</div>
  <div class="script" style="left:36px;top:120px;font-size:36px;transform:rotate(-12deg)">with</div>
  <div class="headline-amount" style="left:62px;top:164px;font-size:58px">$</div>
  <div class="headline-amount" style="left:98px;top:62px;font-size:150px;letter-spacing:-6px">35</div>
  <div class="script" style="left:282px;top:82px;font-size:50px;transform:rotate(-70deg)">off</div>
  <div class="script" style="left:118px;top:238px;font-size:40px;transform:rotate(-28deg)">your next</div>
  <div class="script" style="left:210px;top:272px;font-size:40px;transform:rotate(-28deg)">job</div>

  <p class="services-lead">Our services are: ⟶</p>
  <p class="services-row">PLUMBING<span>|</span>HOT WATER<span>|</span>ELECTRICAL</p>

  <svg class="abs" style="left:0;top:380px" width="774" height="220" aria-hidden="true">
    <path d="M0 62 Q 240 0 476 14 Q 640 22 774 58 L774 220 L0 220 Z" fill="var(--white)"/>
  </svg>

  <div class="brand" style="top:476px">
    <div class="brand-name">HARBOUR TRADES</div>
    <div class="brand-tag">Plumbing • Electrical • Hot Water</div>
  </div>
</section>

<section class="panel back">
  <div class="abs" style="left:0;top:0;width:556px;height:600px;background:var(--orange)"></div>
  <svg class="abs" style="left:548px;top:0" width="60" height="440" aria-hidden="true">
    <rect x="4" y="0" width="52" height="440" fill="var(--blue)"/>
    <rect x="4" y="0" width="10" height="440" fill="var(--blue-dark)"/>
    <rect x="0" y="96" width="60" height="60" rx="4" fill="var(--blue)"/>
    <rect x="0" y="96" width="60" height="8" rx="3" fill="var(--blue-dark)"/>
    <rect x="0" y="148" width="60" height="8" rx="3" fill="var(--blue-dark)"/>
  </svg>
  <div class="photo" role="img" aria-label="Hand tightening a chrome sink trap with a red pipe wrench" style="left:604px;top:0;width:170px;height:440px;background:linear-gradient(180deg,#f2f2f2 0%,#d9c9b6 35%,#b9a690 70%,#a99783 100%)"></div>

  <svg class="abs" style="left:0;top:0" width="774" height="600" aria-hidden="true">
    <path d="M0 442 C 150 400 330 386 450 390 C 540 393 600 410 620 420 L 774 440 L774 600 L0 600 Z" fill="var(--white)"/>
  </svg>

  <p class="voucher-note">*This voucher is<br>&nbsp;&nbsp;valid for the next job</p>

  <div class="script call-word">call</div>
  <svg class="abs" style="left:198px;top:30px" width="58" height="48" aria-label="Phone icon" role="img">
    <path d="M6 18 Q24 4 42 18 L38 24 L32 20 L16 20 L10 24 Z" fill="var(--white)"/>
    <rect x="10" y="24" width="32" height="20" rx="4" fill="var(--white)"/>
    <g fill="var(--orange)"><circle cx="20" cy="30" r="2"/><circle cx="26" cy="30" r="2"/><circle cx="32" cy="30" r="2"/><circle cx="20" cy="37" r="2"/><circle cx="26" cy="37" r="2"/><circle cx="32" cy="37" r="2"/></g>
    <path d="M46 8 Q52 14 50 22 M50 4 Q58 12 55 24" fill="none" stroke="var(--white)" stroke-width="2"/>
  </svg>
  <div class="script one-number">One number</div>
  <p class="tagline-sub">for the best in 3 Trades</p>

  <p class="brief-title">Our services brief:</p>
  <ul class="brief-list">
    <li><svg width="12" height="10" viewBox="0 0 12 10"><path d="M1 5 L4.5 8.5 L11 1" fill="none" stroke="#fff" stroke-width="2"/></svg>Lorem ipsum dolor sit amet,<br>consectetur adipiscing elit.</li>
    <li><svg width="12" height="10" viewBox="0 0 12 10"><path d="M1 5 L4.5 8.5 L11 1" fill="none" stroke="#fff" stroke-width="2"/></svg>Sed eu libero vitae arcu tristique ornare<br>nec ut augue.</li>
    <li><svg width="12" height="10" viewBox="0 0 12 10"><path d="M1 5 L4.5 8.5 L11 1" fill="none" stroke="#fff" stroke-width="2"/></svg>Donec lobortis ligula vel diam<br>condimentum interdum.</li>
    <li><svg width="12" height="10" viewBox="0 0 12 10"><path d="M1 5 L4.5 8.5 L11 1" fill="none" stroke="#fff" stroke-width="2"/></svg>Phasellus vel ante vehicula, commodo<br>odio ut, consequat tortor.</li>
    <li><svg width="12" height="10" viewBox="0 0 12 10"><path d="M1 5 L4.5 8.5 L11 1" fill="none" stroke="#fff" stroke-width="2"/></svg>Integer nec quam quis purus porta<br>lacinia et non libero.</li>
  </ul>

  <div class="photo" role="img" aria-label="Water running into a steel sink drain" style="left:387px;top:26px;width:103px;height:82px;background:radial-gradient(circle,#2a2a2a 0%,#9aa1a6 35%,#e4e6e8 80%)"></div>
  <div class="trade-label label-plumbing" style="left:362px;top:104px;width:140px">PLUMBING</div>
  <div class="photo" role="img" aria-label="Technician adjusting a hot water system" style="left:384px;top:156px;width:102px;height:74px;background:linear-gradient(135deg,#3a5e9c,#e8ecef 60%,#bfc5ca)"></div>
  <div class="trade-label label-hotwater" style="left:364px;top:230px;width:150px">HOT WATER</div>
  <div class="photo" role="img" aria-label="Hands stripping coloured electrical wires" style="left:384px;top:282px;width:102px;height:86px;background:linear-gradient(135deg,#d9b08e,#b46a3c 50%,#e6c3a5)"></div>
  <div class="trade-label label-electrical" style="left:354px;top:366px;width:172px">ELECTRICAL</div>

  <ul class="contact" style="top:458px">
    <li style="top:0"><svg width="12" height="16" viewBox="0 0 12 16" style="top:2px"><path d="M6 15 C2 10 1 8 1 6 A5 5 0 0 1 11 6 C11 8 10 10 6 15 Z" fill="var(--orange)"/><circle cx="6" cy="6" r="2" fill="#fff"/></svg><span style="font-size:15.5px;line-height:17px">123 Street Name,<br>22150 City Name, State (123456)</span></li>
    <li style="top:48px"><svg width="10" height="17" viewBox="0 0 10 17" style="top:3px"><rect x="1" y="1" width="8" height="15" rx="1.5" fill="var(--orange)"/><rect x="2.5" y="3" width="5" height="7" fill="#fff"/></svg><span style="font-size:20px;top:-2px">01234 56789</span></li>
    <li style="top:82px"><svg width="14" height="10" viewBox="0 0 14 10" style="top:4px"><rect width="14" height="10" fill="var(--orange)"/><path d="M0 0 L7 6 L14 0" fill="none" stroke="#fff" stroke-width="1.2"/></svg><span style="font-size:16px">info@yourmailhere.com</span></li>
    <li style="top:110px"><svg width="14" height="14" viewBox="0 0 14 14" style="top:2px"><circle cx="7" cy="7" r="6.5" fill="var(--orange)"/><path d="M0.5 7 H13.5 M7 0.5 V13.5 M7 0.5 C3 4 3 10 7 13.5 C11 10 11 4 7 0.5" fill="none" stroke="#fff" stroke-width=".9"/></svg><span style="font-size:16px">www.yourweb.com</span></li>
  </ul>

  <div class="brand" style="top:478px">
    <div class="brand-name">HARBOUR TRADES</div>
    <div class="brand-tag">Plumbing • Electrical • Hot Water</div>
  </div>
</section>

</body>
</html>
```